Financial Broker firm looking for Brochure design/Pdf-document

Job Type
Brochure Design/PDF-Document
Task Outline
Create a Brochure Design that also works for sending as pdf-document.
Task Description
We need a combined corporate brochure (Booklet style) to give out to potential clients as well as sending it to potential clients through Internet as pdf-document.
We need a background template with pictures and colors that gives the impression of professionalism, trustworthiness and seriousness. Attached text in English but the text will be translated into different languages to fit different markets. Therefore we would like to receive one template including the text and one without any text (but with the logo). Please inform us where (any) pictures and/or photos on the template have been taken from in order for us to buy and use them legally.
About Us
Our company Quelvant Partners AB is a financial brokerage company who provides a diversity of services for different selected partners (www.quelvantpartners.example).
Target Market
Companies on all levels, domestic or international
Requirements
Must Have:
-The text and logo attached below
Industry/Entity Type
Financial
Look and feel

```html
<!DOCTYPE html>
<html lang="en">
<head>
<meta charset="utf-8">
<title>Quelvant Partners AB – Bonding &amp; Factoring spread</title>
<link rel="stylesheet" href="https://fonts.googleapis.com/css2?family=Arimo:wght@700&family=Roboto:wght@300;400&display=swap">
<style>
  :root {
    --page-white: #ffffff;
    --ink-black: #050505;
    --navy: #0b1e3a;
    --cyan: #1ee3f0;
    --sky-blue: #29b2f2;
    --panel-grey: #cbcbcb;
    --box-grey: #9a9a9a;
    --body-text: #1e1e1e;
    --shadow: rgba(0,0,0,0.18);
  }
  * { box-sizing: border-box; margin: 0; padding: 0; }
  html, body { width: 1200px; height: 1000px; overflow: hidden; background: var(--page-white); }
  .canvas { position: relative; width: 1200px; height: 1000px; }
  .spread {
    position: absolute; left: 134px; top: 152px; width: 935px; height: 701px;
    background: var(--page-white);
    box-shadow: 0 4px 14px var(--shadow);
    overflow: hidden;
  }
  .block { position: absolute; }
  .left-top-band { left: 0; top: 0; width: 467px; height: 119px; background: var(--ink-black); }
  .right-grey-panel { left: 467px; top: 124px; width: 468px; height: 369px; background: var(--panel-grey); }
  .title-bar { left: 63px; top: 60px; width: 809px; height: 59px; background: var(--navy); }
  .page-divider { left: 467px; top: 0; width: 1px; height: 701px; background: #d6d6d6; }

  .section-title {
    position: absolute; font-family: "Arimo", Arial, sans-serif; font-weight: 700;
    font-size: 22px; color: var(--cyan); line-height: 1;
  }
  .title-bonding { left: 76px; top: 77px; }
  .title-factoring { left: 545px; top: 77px; }

  .photo { position: absolute; }
  .photo-meeting {
    left: 63px; top: 125px; width: 359px; height: 226px;
    background: linear-gradient(135deg, #e9edf2 0%, #cfd6de 45%, #3a4352 70%, #eef1f4 100%);
  }
  .photo-market {
    left: 467px; top: 493px; width: 399px; height: 208px;
    background: linear-gradient(160deg, #2a4a7a 0%, #13203a 40%, #1c3a2a 70%, #0c0f16 100%);
  }
  .right-bottom-black { left: 866px; top: 493px; width: 69px; height: 208px; background: var(--ink-black); }

  .copy {
    position: absolute; font-family: "Roboto", Helvetica, Arial, sans-serif; font-weight: 300;
    font-size: 14px; line-height: 20px; color: var(--body-text); letter-spacing: -0.2px;
  }
  .copy p { text-align: justify; }
  .bonding-copy { left: 63px; top: 358px; width: 362px; letter-spacing: -0.35px; word-spacing: -0.5px; }

  .factoring-copy { left: 511px; top: 135px; width: 355px; }
  .factoring-copy p + p, .factoring-copy ul + p { margin-top: 4px; }
  .factoring-copy .lead-in { text-align: left; }
  .benefits { list-style: none; margin-top: 2px; }
  .benefits li { position: relative; padding-left: 13px; }
  .benefits li::before { content: "·"; position: absolute; left: 1px; top: 0; }
  .factoring-copy .closing { text-align: left; letter-spacing: -0.3px; }

  .collection-bar { left: 63px; top: 493px; width: 404px; height: 38px; background: var(--ink-black); }
  .collection-title {
    position: absolute; left: 76px; top: 503px; font-family: "Arimo", Arial, sans-serif;
    font-size: 21px; color: var(--cyan); line-height: 1; font-weight: 700;
  }
  .collection-title .light { font-family: "Roboto", Helvetica, Arial, sans-serif; font-weight: 400; }
  .collection-box { left: 0; top: 531px; width: 467px; height: 139px; background: var(--box-grey); }
  .collection-copy { left: 63px; top: 537px; width: 360px; color: #ffffff; font-size: 14.4px; line-height: 20.5px; letter-spacing: -0.1px; }
  .bottom-blue { left: 122px; top: 670px; width: 345px; height: 31px; background: var(--sky-blue); }
</style>
</head>
<body>
<div class="canvas">
  <div class="spread">
    <div class="block left-top-band"></div>
    <div class="block right-grey-panel"></div>
    <div class="block title-bar"></div>

    <h2 class="section-title title-bonding">Bonding</h2>
    <h2 class="section-title title-factoring">Factoring</h2>

    <div class="photo photo-meeting" role="img" aria-label="Overhead photo of business people shaking hands across a meeting table with charts and a laptop"></div>

    <div class="copy bonding-copy">
      <p>Our insurance partners can issue bonds on behalf of its clients throughout the world, for almost all sectors of any industry and commerce. Your company has the advantage of being able to compete for a contract knowing that a bond will be available within the agreed underwriting criteria. Your credit line and working capital isthereby safeguarded.</p>
    </div>

    <div class="copy factoring-copy">
      <p>Factoring is a financial transaction whereby you as a company have the possibility to sell, or lend on, your account receivables (invoices) to a (pre)agreed rate. Compared to lending money where the focus is on your credit worthiness, factoring shifts the focus to your customers' credit rating.</p>
      <p class="lead-in">Your benefits with mortgage or selling your invoices are:</p>
      <ul class="benefits">
        <li>Accelerated cash flow through faster collections</li>
        <li>Liquidity to boost working capital</li>
        <li>Increased sales in foreign markets by offering competitive terms of sale</li>
        <li>Opportunity to use supplier discounts</li>
        <li>Protection against credit losses (when selling your invoices to a factoring company)</li>
      </ul>
      <p class="closing">Depending on your need, demand, domestic or export, we will find a factoring company that will provide you with a solution that is right for your company.</p>
    </div>

    <div class="block collection-bar"></div>
    <h2 class="collection-title">Trade debt <span class="light">collection</span></h2>
    <div class="block collection-box"></div>
    <div class="copy collection-copy">
      <p>Another benefit with our insurance partners is that they offer a trade debt collections service that corresponds to your company. They have experience in recognition of customers' needs, not only to secure full payment as quickly as possible, but also to maintain a good relationship with clients.</p>
    </div>
    <div class="block bottom-blue"></div>

    <div class="photo photo-market" role="img" aria-label="Photo of stock market screens with two dice reading buy and sell"></div>
    <div class="block right-bottom-black"></div>
    <div class="block page-divider"></div>
  </div>
</div>
</body>
</html>
```